Web Design Front Page Only for Organic Skincare

We have been in business for nearly 20 years. We are run by all females and sell anything from aromatherapy, skincare and pharmacy types products to health food shops and pharmacy. We are looking for an attractive and colourful but simple front web page design for our wholesale customers to look at. We want our customers to start using our website to find information rather than ringing us. So we want it to be attractive to our buyers who are young and funky.
Updates

To give you an idea of the products we sell to pharmacy and health food shops also beauty shops and hair salons.  We mainly deal with organic body and skincare, aromatherapy oils and body products, but also do some simple pharmacy products such as bandages and pill boxes, finger splits, walking frames and wheelchairs.  We are only looking for the front page of the website.  The back-end will be done in-house.  We currently do not have a logo designed so I am thinking that once we have done the website design we can build a logo from it.  I like bright colours and want something that is inviting to further discover that we do many different types of products.

Target Market(s)

young girls who are our retail buyers

Industry/Entity Type

Pharmacy

Requirements
Must have
• A section which says

Customer Log in
Should not have
• don't worry about too much writing or tabs. We will insert these later. Just come up with design image.

```html
<!DOCTYPE html>
<html lang="en">
<head>
<meta charset="utf-8">
<title>Verdelle Healthcare – Wholesale Home</title>
<link rel="stylesheet" href="https://fonts.googleapis.com/css2?family=Questrial&family=Montserrat:wght@300;400;600&display=swap">
<style>
  :root {
    --sky-mid: #a9e2e6;
    --teal-text: #27a6b2;
    --teal-soft: #6ccad3;
    --teal-band: #2fb0bb;
    --skin-pale: #b3e5ec;
    --leaf: #9bc43a;
    --login-green: #a9d68c;
    --violet: #9a5cc2;
    --violet-dark: #8d4fb8;
    --lavender-deep: #8f6bbf;
    --lavender-soft: #b9a3db;
    --lavender-mist: #e6def2;
    --bark: #6b4c1e;
    --arrow-grey: #a99c8c;
    --panel: #fbfafa;
    --sidebar-top: #ffffff;
    --sidebar-bottom: #ebe9e8;
    --footer-link: #e6ef9c;
    --white: #ffffff;
  }
  * { box-sizing: border-box; margin: 0; padding: 0; }
  html, body { width: 1200px; height: 860px; overflow: hidden; }
  body {
    position: relative;
    font-family: "Questrial", "Century Gothic", sans-serif;
    background:
      radial-gradient(ellipse 420px 600px at 40px 430px, rgba(255,255,255,.75), rgba(255,255,255,0) 70%),
      radial-gradient(ellipse 420px 600px at 1160px 430px, rgba(255,255,255,.7), rgba(255,255,255,0) 70%),
      linear-gradient(180deg, var(--sky-mid) 0%, #7fd0d8 60%, #52bfc9 100%);
  }

  /* header */
  .site-header {
    position: absolute; left: 0; top: 0; width: 1200px; height: 142px;
    background: linear-gradient(180deg, #f1fbfb 0%, #d7f1f3 55%, #bfe8ec 100%);
    overflow: hidden;
  }
  .header-swoosh { position: absolute; left: 0; top: 0; }
  .customer-login {
    position: absolute; left: 1033px; top: 0; width: 142px; height: 46px;
    background: var(--login-green);
    color: var(--white); font-size: 15px; text-decoration: underline;
    display: flex; align-items: center; padding-left: 13px;
  }
  .customer-login .caret { font-size: 8px; margin-left: 9px; display: inline-block; }
  .brand {
    position: absolute; left: 180px; top: 46px;
    color: var(--leaf); font-size: 27px; line-height: 29px; letter-spacing: .5px;
    text-transform: uppercase;
  }
  .utility-nav {
    position: absolute; left: 550px; top: 57px;
    font-size: 13px; color: var(--teal-text);
  }
  .utility-nav a { color: var(--teal-text); text-decoration: none; }
  .utility-nav .sep { margin: 0 9px; }
  .search-field {
    position: absolute; left: 549px; top: 79px; width: 363px; height: 37px;
    background: #fbfdf0; border: 1px solid #b3b9b4;
    font-size: 15px; color: #555; padding: 9px 9px;
  }
  .search-button {
    position: absolute; left: 920px; top: 79px; width: 103px; height: 36px;
    background: linear-gradient(180deg, #c5e57a 0%, #9bcb3b 100%);
    border: 1px solid #8fbd33; border-radius: 2px;
    color: var(--white); font-family: "Montserrat", sans-serif; font-weight: 600; font-size: 18px;
    display: flex; align-items: center; justify-content: center;
  }

  /* main nav */
  .main-nav {
    position: absolute; left: 0; top: 142px; width: 1200px; height: 45px;
    background: linear-gradient(180deg, #8fd8e0 0%, #6cc7d1 50%, #55bcc6 100%);
    box-shadow: 0 3px 4px rgba(0,80,90,.18);
    z-index: 2;
  }
  .main-nav a {
    position: absolute; top: 0; height: 45px; line-height: 45px;
    color: var(--white); text-decoration: none; font-size: 14px; text-transform: uppercase;
    transform: translateX(-50%);
  }
  .main-nav a.is-current { font-family: "Montserrat", sans-serif; font-weight: 600; }
  .main-nav .divider { position: absolute; top: 0; width: 1px; height: 45px; background: rgba(255,255,255,.55); }

  /* page panel */
  .page {
    position: absolute; left: 183px; top: 187px; width: 838px; height: 625px;
    background: var(--panel);
    box-shadow: 0 0 6px rgba(0,70,80,.25);
  }
  .sidebar {
    position: absolute; left: 0; top: 0; width: 184px; height: 625px;
    background: linear-gradient(180deg, var(--sidebar-top) 0%, var(--sidebar-bottom) 100%);
  }
  .sidebar-photo {
    position: absolute; left: 0; top: 8px; width: 127px; height: 84px;
    background:
      linear-gradient(155deg, var(--lavender-soft) 0%, var(--lavender-deep) 45%, var(--lavender-soft) 75%, var(--lavender-mist) 100%);
    border-radius: 0 4px 4px 0;
  }
  .categories-title {
    position: absolute; left: 20px; top: 103px;
    font-family: "Montserrat", sans-serif; font-weight: 600; font-size: 13px; color: var(--violet-dark);
  }
  .category-list { position: absolute; left: 18px; top: 129px; width: 155px; list-style: none; }
  .category-list li {
    height: 33.6px; line-height: 34px; padding-left: 2px;
    font-size: 15px; color: var(--violet);
    border-bottom: 1px solid #dcd8d6;
  }
  .category-list li:last-child { border-bottom: none; }
  .category-list .caret { font-size: 8px; color: var(--arrow-grey); margin-left: 7px; vertical-align: 2px; }

  .content {
    position: absolute; left: 184px; top: 0; width: 638px; height: 610px;
    background: linear-gradient(180deg, #ffffff 0%, #fbfafa 100%);
  }
  .eyebrow {
    position: absolute; left: 39px; top: 74px;
    font-size: 19px; color: var(--teal-soft); letter-spacing: .3px;
  }
  .headline {
    position: absolute; left: 38px; top: 96px;
    font-family: "Montserrat", sans-serif; font-size: 62px; line-height: 70px; white-space: nowrap;
  }
  .headline .love { color: var(--teal-text); font-weight: 600; letter-spacing: -4px; }
  .headline .your { color: var(--leaf); font-weight: 300; letter-spacing: -5px; margin-left: 16px; }
  .headline .skin { color: var(--skin-pale); font-weight: 400; letter-spacing: 4px; margin-left: 13px; }
  .tagline {
    position: absolute; left: 39px; top: 164px;
    font-size: 15px; line-height: 17px; color: var(--bark);
  }
  .product { position: absolute; font-size: 15px; color: var(--teal-text); }
  .see-all {
    position: absolute; left: 481px; top: 559px;
    font-size: 15px; line-height: 17px; color: var(--teal-text);
  }
  .see-all .caret { font-size: 8px; color: var(--arrow-grey); margin-left: 6px; vertical-align: 2px; letter-spacing: -1px; }

  /* footer */
  .site-footer {
    position: absolute; left: 0; top: 812px; width: 1200px; height: 48px;
    background: var(--teal-band);
  }
  .copyright { position: absolute; left: 184px; top: 18px; font-size: 13px; color: var(--white); }
  .footer-nav { position: absolute; right: 179px; top: 16px; font-size: 13px; color: var(--footer-link); }
  .footer-nav .sep { margin: 0 14px; }
</style>
</head>
<body>

<header class="site-header">
  <svg class="header-swoosh" width="1200" height="142" viewBox="0 0 1200 142" aria-hidden="true">
    <path d="M0 70 C 300 20, 700 140, 1200 40 L1200 60 C 700 160, 300 40, 0 95 Z" fill="#ffffff" opacity=".35"/>
    <path d="M250 0 C 500 60, 800 70, 1200 110 L1200 142 C 800 95, 500 80, 200 0 Z" fill="#ffffff" opacity=".25"/>
  </svg>
  <a class="customer-login" href="#">customer log in<span class="caret">&#9654;</span></a>
  <div class="brand">Verdelle<br>Healthcare</div>
  <nav class="utility-nav">
    <a href="#">home</a><span class="sep">|</span><a href="#">contact us</a><span class="sep">|</span><a href="#">wholesalers</a><span class="sep">|</span><a href="#">newsletter</a>
  </nav>
  <div class="search-field">Search entire site...</div>
  <div class="search-button">Search</div>
</header>

<nav class="main-nav">
  <a class="is-current" href="#" style="left:314px">Home</a>
  <span class="divider" style="left:367px"></span>
  <a href="#" style="left:452px">Health Food</a>
  <span class="divider" style="left:533px"></span>
  <a href="#" style="left:607px">Pharmacy</a>
  <span class="divider" style="left:680px"></span>
  <a href="#" style="left:760px">Supermarket</a>
  <span class="divider" style="left:839px"></span>
  <a href="#" style="left:898px">Beauty</a>
</nav>

<main class="page">
  <aside class="sidebar">
    <div class="sidebar-photo" role="img" aria-label="Photo of a bunch of lavender sprigs"></div>
    <h2 class="categories-title">CATEGORIES</h2>
    <ul class="category-list">
      <li>Face<span class="caret">&#9654;</span></li>
      <li>Body<span class="caret">&#9654;</span></li>
      <li>Hair<span class="caret">&#9654;</span></li>
      <li>Aromatherapy<span class="caret">&#9654;</span></li>
      <li>Pharmacy<span class="caret">&#9654;</span></li>
      <li>Beauty<span class="caret">&#9654;</span></li>
      <li>Skincare<span class="caret">&#9654;</span></li>
      <li>Best Sellers<span class="caret">&#9654;</span></li>
      <li>View All Products<span class="caret">&#9654;</span></li>
    </ul>
  </aside>

  <section class="content">
    <p class="eyebrow">NEW PRODUCTS</p>
    <h1 class="headline"><span class="love">LOVE</span><span class="your">YOUR</span><span class="skin">SKIN</span></h1>
    <p class="tagline">Take care of skin with<br>natural, organic products.</p>

    <span class="product" style="left:77px;top:310px">Product</span>
    <span class="product" style="left:273px;top:310px">Product</span>
    <span class="product" style="left:477px;top:310px">Product</span>
    <span class="product" style="left:77px;top:460px">Product</span>
    <span class="product" style="left:273px;top:460px">Product</span>
    <span class="product" style="left:477px;top:460px">Product</span>

    <a class="see-all">See all new<br>organic skincare<span class="caret">&#9654;&#9654;</span></a>
  </section>
</main>

<footer class="site-footer">
  <p class="copyright">2012 Verdelle Healthcare&nbsp; All Rights Reserved</p>
  <nav class="footer-nav">ordering<span class="sep">|</span>terms &amp; conditions<span class="sep">|</span>privacy policy</nav>
</footer>

</body>
</html>
```